Rise Past Horizon needs a new design for Business Cards

We need a business card design for our personal training business call Rise Past Horizon. We are the Sustained Weight Loss Specialists.
Our target market is overweight and obese adults who have experience the ups of loosing weight and lows of putting it back on and are looking for a sustained weight loss solution.
Our USP is: "We Smash Through The Barriers That Are Holding You Back From Sustained Weight Loss".
We would like to the design incorporate the colours of our logo, with other acceptable colours being black, white, yellow and green.
Visit our website at www.risepasthorizon.com.au for an overview of our business, and also the attached company profile.

Target Market(s)

Industry/Entity Type

Training

Colors
0092cd
eb1f27
fbed22
9bcb3c
000000
ffffff

Requirements
Must have
• Easy to read fonts
Logo (Not huge)
Call to Action (Something like, Claim your 10 Tips to Melt Body Fat, and 30 minutes PT Session VALUED AT $101)
Contact and Address details (as per footer of company profile (page 2 onwards)
List of Benefits (see company profile and website)
USP as per project overview
A picture to match the USP
Should not have
• Please do not try and copy the design of the company profile. It was slapped together.
A list of exercises

```html
<!DOCTYPE html>
<html lang="en">
<head>
<meta charset="utf-8">
<title>Rise Past Horizon – Business Cards</title>
<link href="https://fonts.googleapis.com/css2?family=Anton&family=Oswald:wght@400;600;700&family=Roboto+Condensed:wght@400;700&display=swap" rel="stylesheet">
<style>
  :root{
    --bg:#e6e6e6;
    --card:#f4f4f4;
    --card-edge:#dcdcdc;
    --blue:#3d5fae;
    --blue-dark:#2b4a92;
    --blue-light:#6f8fd0;
    --red:#d3283a;
    --ice:#7fb7c9;
    --grey-text:#6a6a6a;
    --white:#ffffff;
  }
  *{margin:0;padding:0;box-sizing:border-box}
  html,body{width:1200px;height:1000px;overflow:hidden;background:var(--bg)}
  .sheet{position:relative;width:1200px;height:1000px}
  .card{position:absolute;left:210px;width:780px;height:446px;border-radius:22px;overflow:hidden;
    background:linear-gradient(135deg,#fbfbfb 0%,var(--card) 55%,var(--card-edge) 100%);
    box-shadow:0 6px 18px rgba(0,0,0,.18)}
  .card--front{top:34px}
  .card--back{top:520px}

  /* front */
  .front-band{position:absolute;left:0;top:0;width:780px;height:446px}
  .smash-art{position:absolute;left:40px;top:160px;width:200px;height:150px;border-radius:10px;
    background:radial-gradient(circle at 45% 50%,#c9e3ec 0%,var(--ice) 55%,var(--blue-light) 100%)}
  .headline{position:absolute;left:250px;top:34px;font-family:'Anton',sans-serif;color:var(--blue);line-height:.95;text-transform:uppercase}
  .headline__lead{display:block;font-size:52px;letter-spacing:1px}
  .headline__main{display:block;font-size:128px;letter-spacing:2px;color:var(--blue-dark);margin-top:4px}
  .usp-sub{position:absolute;left:250px;top:292px;font-family:'Oswald',sans-serif;font-weight:700;font-size:20px;color:var(--blue);white-space:nowrap}
  .usp-sub em{font-style:normal;color:var(--red)}
  .front-url{position:absolute;right:34px;bottom:24px;font-family:'Oswald',sans-serif;font-weight:700;font-size:22px;color:var(--white);letter-spacing:.5px}

  /* back */
  .training-photo{position:absolute;left:0;top:0;width:780px;height:446px}
  .cta{position:absolute;right:36px;top:64px;text-align:right;font-family:'Oswald',sans-serif;font-weight:700;font-size:27px;line-height:1.18;color:var(--red)}
  .cta strong{color:var(--white);font-weight:700}
  .brand{position:absolute;left:40px;top:290px;display:flex;flex-direction:column;align-items:flex-start;gap:10px}
  .brand__dot{width:22px;height:22px;border-radius:50%;background:var(--red)}
  .brand__name{font-family:'Oswald',sans-serif;font-weight:600;font-size:18px;color:var(--red);letter-spacing:1px;text-transform:uppercase;white-space:nowrap}
  .contacts{position:absolute;left:240px;top:262px;font-family:'Roboto Condensed',sans-serif;color:var(--grey-text)}
  .contact{margin-bottom:8px}
  .contact__line{font-size:22px;font-weight:700;color:#555;line-height:1.2}
  .contact__name{color:var(--blue)}
  .contact__meta{font-size:11px;line-height:1.3}
  .back-url{font-family:'Oswald',sans-serif;font-weight:600;font-size:18px;color:var(--blue);margin-top:2px}
  .address{font-size:12px;color:var(--grey-text)}
</style>
</head>
<body>
<main class="sheet">

  <section class="card card--front" aria-label="Card front">
    <svg class="front-band" viewBox="0 0 780 446" aria-hidden="true">
      <path d="M260 446 C 400 380, 600 345, 780 330 L780 446 Z" fill="var(--red)"/>
      <path d="M290 446 C 420 392, 610 358, 780 344 L780 446 Z" fill="var(--blue)"/>
    </svg>
    <div class="smash-art" role="img" aria-label="Illustration of a fist smashing through a barrier"></div>
    <h1 class="headline">
      <span class="headline__lead">We Smash<br>Through The</span>
      <span class="headline__main">Barriers</span>
    </h1>
    <p class="usp-sub">That Are Holding You Back From Sustained <em>Weight Loss</em></p>
    <p class="front-url">www.risepasthorizon.com.au</p>
  </section>

  <section class="card card--back" aria-label="Card back">
    <svg class="training-photo" viewBox="0 0 780 446">
      <defs>
        <linearGradient id="photoTone" x1="0" y1="0" x2="1" y2="0.4">
          <stop offset="0" stop-color="#c99a86"/>
          <stop offset="0.35" stop-color="#d4506a"/>
          <stop offset="0.6" stop-color="#3a4f8c"/>
          <stop offset="1" stop-color="#1f2f66"/>
        </linearGradient>
      </defs>
      <g role="img" aria-label="Photo of a trainer measuring a client's waist with a tape measure">
        <path d="M300 0 L780 0 L780 200 C 620 240, 450 240, 300 195 Z" fill="url(#photoTone)"/>
      </g>
      <path d="M300 195 C 450 240, 620 240, 780 200 L780 216 C 620 256, 450 256, 300 211 Z" fill="var(--red)"/>
      <path d="M240 150 C 275 180, 300 195, 330 205 C 290 205, 260 190, 240 172 Z" fill="var(--blue-light)"/>
    </svg>
    <p class="cta">CLAIM YOUR <strong>10 TIPS</strong><br>to Melt Body Fat, and 30 minutes<br>PT Session <strong>VALUED AT $101</strong></p>

    <div class="brand">
      <span class="brand__dot"></span>
      <p class="brand__name">Rise Past Horizon</p>
    </div>
    <div class="contacts">
      <div class="contact">
        <p class="contact__line"><span class="contact__name">MARCUS</span> 0400 555 218</p>
        <p class="contact__meta">marcus@risepasthorizon.com.au<br>Manager</p>
      </div>
      <div class="contact">
        <p class="contact__line"><span class="contact__name">RHYS</span> 0400 555 218</p>
        <p class="contact__meta">rhys@risepasthorizon.com.au<br>Head Trainer</p>
      </div>
      <p class="back-url">www.risepasthorizon.com.au</p>
      <p class="address">14 Wattle Grove Rd, Parkfield, QLD 4000</p>
    </div>
  </section>

</main>
</body>
</html>
```